Singer/Songwriter Artist Promotion Website

***DO NOT CONTACT ME PRIVATELY***

I need a fresh, exciting, upbeat-looking site. The purpose of our business is to genuinely promote unknown, unsigned music artists. The sight initially needs a feel slanted toward Country Music.

DESIGN
The website design should be similar to this site;
https://www.pelvarotune.com

For the design, make it follow a linear flow of sections/blocks. We don't want a complex design with objects/images in random parts of the page, but rather section "blocks" of content.

I need 5 pages designed;
Home
FAQ
Our Staff
"Launch Your Music" This page is more complex. This page needs to display a questionnaire that can be filled out. This page will need to be able to capture and process payments. There needs to be a way to attach files for upload.
"Artist Profiles" - > A template page that will be used for multiple artists. It will show the artist/musician information

Design/Colors
I want colors that are attractive, professional but exciting. I’m looking for tasteful, interesting, eye-catching, not boring.

Taglines;
Name: “Bluefield Tunecast Circle”
Tagline: “All Original Artists-All Original Country
24/7, Commercial Free, All The Time”

LOGO DESIGN
- See attached basic logo
Bluefield Tunecast Circle
BTC
Base design off of attached logo. I’d like the "Bluefield Tunecast Circle" to be Colorful. Attention getting. Possibly showing some movement. Maybe a gradient.

Target Market(s)

Independent Musicians

Industry/Entity Type

Songwriting, Music Promotion, Radio Network

Number of Pages Required

5+ page

Colors
00AB8E
00BBA5
67D7C9
C6EFE9
E9F9F6

```html
<!DOCTYPE html>
<html lang="en">
<head>
<meta charset="utf-8">
<title>Bluefield Tunecast Circle</title>
<link href="https://fonts.googleapis.com/css2?family=Michroma&family=Poppins:wght@400;500;600;700&display=swap" rel="stylesheet">
<style>
:root{
  --blue:#2b55e0;
  --blue-deep:#1d2f9e;
  --navy:#151c6b;
  --ink:#0b1030;
  --text:#4a4f66;
  --soft:#eef1fa;
  --white:#ffffff;
  --sky:#4d8cff;
}
*{box-sizing:border-box;margin:0;padding:0}
html,body{width:1200px;height:5164px;overflow:hidden}
body{font-family:"Poppins",sans-serif;color:var(--text);background:var(--white);position:relative}
.display{font-family:"Michroma",sans-serif;text-transform:uppercase}
section,header,footer{position:absolute;left:0;width:1200px}
.abs{position:absolute}
.btn{position:absolute;display:flex;align-items:center;justify-content:center;font-size:12px;font-weight:600;letter-spacing:1px;text-transform:uppercase}

/* header */
.site-header{top:0;height:120px;background:var(--white)}
.brand{left:88px;top:34px;font-family:"Michroma",sans-serif;font-size:40px;color:var(--navy);letter-spacing:2px}
.call-strip{right:0;top:0;width:370px;height:40px;background:var(--navy);border-bottom-left-radius:40px;color:var(--white);font-size:13px;display:flex;align-items:center;padding-left:70px;gap:10px}
.nav{left:490px;top:68px;display:flex;gap:44px;font-size:14px;font-weight:500;color:var(--ink);text-transform:uppercase}
.nav .active{color:var(--blue);border-bottom:2px solid var(--blue);padding-bottom:6px}

/* hero */
.hero{top:120px;height:520px;background:linear-gradient(100deg,#1b3cc7,#3a7af0 50%,#2044c8);overflow:hidden}
.hero-photo{left:0;top:0;width:1200px;height:520px;background:radial-gradient(circle at 50% 40%,rgba(130,190,255,.35),rgba(20,40,160,0) 60%)}
.hero-mark{left:0;width:1200px;top:60px;text-align:center;font-family:"Michroma",sans-serif;font-size:180px;line-height:200px;color:rgba(255,255,255,.28);letter-spacing:20px}
.hero-title{left:0;width:1200px;top:262px;text-align:center;color:var(--white);font-size:34px;line-height:50px;letter-spacing:2px}
.hero .btn{left:480px;top:396px;width:240px;height:52px;border:2px solid var(--white);color:var(--white)}
.hero-arrow{top:230px}

/* about */
.about{top:640px;height:700px}
.about-frame{left:72px;top:124px;width:296px;height:476px;background:var(--blue)}
.about-photo{left:88px;top:140px;width:296px;height:460px;background:linear-gradient(160deg,#7fa05a,#d9d2c0 60%,#f1ede4)}
.about h2{left:460px;top:150px;font-size:32px;line-height:42px;color:var(--blue)}
.about h2 span{color:var(--ink);display:block}
.about .copy{left:460px;top:290px;width:660px;font-size:15px;line-height:28px}
.about .copy p+p{margin-top:22px}

/* qualifies */
.qualifies{top:1340px;height:748px;background:var(--soft)}
.qualifies h2{left:88px;top:150px;font-size:34px;color:var(--navy)}
.qualifies h2 b{color:var(--blue);font-weight:400}
.qualifies .sub{left:88px;top:196px;font-size:18px;color:var(--blue);letter-spacing:2px}
.ticks{left:88px;top:254px;width:560px;list-style:none;font-size:15px;line-height:26px}
.ticks li{display:flex;gap:14px;margin-bottom:16px}
.ticks svg{flex:none;margin-top:3px}
.qualifies .btn{left:88px;top:502px;width:230px;height:52px;border:2px solid var(--blue);color:var(--blue)}
.q-arc{left:690px;top:110px}
.q-photo{left:740px;top:120px;width:420px;height:420px;border-radius:50%;background:linear-gradient(150deg,#e6dfd6,#b58a64 50%,#3a2d26)}

/* how it works */
.how{top:2088px;height:1200px}
.how h2{left:0;width:1200px;top:122px;text-align:center;font-size:34px;color:var(--navy)}
.how h2 b{color:var(--blue);font-weight:400}
.step{left:88px;width:1024px;height:260px;background:var(--white);border-radius:22px;box-shadow:0 12px 40px rgba(30,50,140,.12);overflow:hidden}
.step-tab{top:0;width:290px;height:260px;background:linear-gradient(135deg,var(--sky),var(--blue-deep));color:var(--white)}
.step-tab .lbl{font-family:"Michroma",sans-serif;font-size:20px;line-height:34px}
.step-tab .lbl b{display:block;font-size:44px;font-weight:400;line-height:56px}
.step-icon{width:90px;height:90px;border-radius:50%;background:var(--white);display:flex;align-items:center;justify-content:center;box-shadow:0 6px 20px rgba(0,0,0,.15)}
.step p{position:absolute;font-size:15px;line-height:27px;width:640px}

/* exposure */
.exposure{top:3288px;height:744px;background:linear-gradient(135deg,#1a2384,#0e1457);overflow:hidden}
.exp-mark{left:0;top:460px;width:1200px;font-family:"Michroma",sans-serif;font-size:230px;color:rgba(255,255,255,.05);text-align:center;letter-spacing:20px}
.exp-frame{left:170px;top:60px;width:300px;height:580px;background:var(--blue)}
.exp-photo{left:190px;top:80px;width:300px;height:580px;background:linear-gradient(180deg,#c9c2b4,#8a8276 60%,#3e3a34)}
.exposure h2{left:540px;top:96px;font-size:34px;line-height:46px;color:var(--white)}
.exposure .sub{left:540px;top:198px;font-size:14px;color:var(--white);letter-spacing:6px;font-weight:600}
.exposure .ticks{left:540px;top:250px;width:560px;color:var(--white)}

/* artists */
.artists{top:4032px;height:748px}
.artists h2{left:0;width:1200px;top:118px;text-align:center;font-size:34px;color:var(--navy)}
.artists h2 b{color:var(--blue);font-weight:400}
.artist{top:200px;width:232px;text-align:center}
.artist .frame{position:absolute;left:-14px;top:-14px;width:232px;height:280px;background:var(--blue)}
.artist .photo{position:relative;width:232px;height:280px}
.artist h3{margin-top:26px;font-family:"Michroma",sans-serif;font-size:15px;line-height:20px;color:var(--ink);font-weight:400;text-transform:uppercase}
.artist span{display:block;font-size:13px;line-height:20px}
.artists .btn{left:480px;top:608px;width:240px;height:52px;background:var(--navy);color:var(--white)}

/* footer */
.site-footer{top:4780px;height:384px;background:var(--ink);color:#c9cde0}
.site-footer .brand{color:var(--white);left:88px;top:70px}
.socials{left:88px;top:170px;display:flex;gap:14px}
.socials i{width:42px;height:42px;border-radius:50%;border:1px solid rgba(255,255,255,.35);display:block}
.copyright{left:88px;top:240px;font-size:13px}
.f-divider{top:50px;width:1px;height:280px;background:rgba(255,255,255,.12)}
.site-footer h4{font-family:"Michroma",sans-serif;font-weight:400;font-size:16px;color:var(--white)}
.links{left:430px;top:70px}
.links ul{list-style:none;margin-top:22px;font-size:14px;line-height:30px}
.news{left:810px;top:70px}
.news .field{margin-top:30px;width:290px;height:48px;border-radius:6px;background:#2a2f4c;font-size:13px;padding:0 16px;display:flex;align-items:center;color:#9aa0bb}
.news .btn{position:relative;margin-top:16px;width:290px;height:48px;border-radius:6px;background:var(--blue);color:var(--white)}
</style>
</head>
<body>

<header class="site-header">
  <div class="abs brand">BTC</div>
  <div class="abs call-strip">
    <svg width="16" height="16" viewBox="0 0 24 24" fill="#fff"><path d="M6.6 10.8a15 15 0 0 0 6.6 6.6l2.2-2.2c.3-.3.7-.4 1-.2 1.1.4 2.3.6 3.6.6.6 0 1 .4 1 1V20c0 .6-.4 1-1 1A17 17 0 0 1 3 4c0-.6.4-1 1-1h3.5c.6 0 1 .4 1 1 0 1.3.2 2.5.6 3.6.1.3 0 .7-.2 1z"/></svg>
    <span>CALL US: 555-014-2290</span>
  </div>
  <nav class="abs nav">
    <span class="active">Home</span><span>Our Staff</span><span>Launch Your Music</span><span>FAQ</span><span>Artist Profiles</span>
  </nav>
</header>

<section class="hero">
  <div class="abs hero-photo" role="img" aria-label="Blue-toned photo of country musicians performing on stage"></div>
  <div class="abs hero-mark">BTC</div>
  <h1 class="abs display hero-title">All Original Artist<br>All Original Country</h1>
  <svg class="abs hero-arrow" style="left:24px" width="24" height="44" viewBox="0 0 24 44"><path d="M20 2 4 22l16 20" stroke="#fff" stroke-width="2.5" fill="none"/></svg>
  <svg class="abs hero-arrow" style="right:24px" width="24" height="44" viewBox="0 0 24 44"><path d="M4 2l16 20L4 42" stroke="#fff" stroke-width="2.5" fill="none"/></svg>
  <span class="btn">View Our Artist</span>
</section>

<section class="about">
  <div class="abs about-frame"></div>
  <div class="abs about-photo" role="img" aria-label="Photo of a songwriter writing lyrics on sheet music outdoors"></div>
  <h2 class="abs display">Bluefield<br>Tunecast Circle<span>Has The Answer!</span></h2>
  <div class="abs copy">
    <p>In the 1990's, the music industry imploded with the closing of large recording studios. At the same time, with the dawning of digital home studios, the number of solid songwriting artists exploded. It is now easier than ever for talented artists to record and release their music but who is listening and how can you reach the masses with to your music?</p>
    <p>We are US based company with DJs based in Australia, Scotland, Germany, England, USA and beyond. Our network of international DJ's offer original songwriting artists a worldwide platform to showcase their songs.</p>
  </div>
</section>

<section class="qualifies">
  <h2 class="abs display"><b>Who</b> Qualifies</h2>
  <div class="abs display sub">For BTC?</div>
  <ul class="abs ticks">
    <li><svg width="20" height="20" viewBox="0 0 20 20"><circle cx="10" cy="10" r="10" fill="#2b55e0"/><path d="m5.5 10 3 3 6-6" stroke="#fff" stroke-width="2" fill="none"/></svg>We accept only original material. (No covers accepted).</li>
    <li><svg width="20" height="20" viewBox="0 0 20 20"><circle cx="10" cy="10" r="10" fill="#2b55e0"/><path d="m5.5 10 3 3 6-6" stroke="#fff" stroke-width="2" fill="none"/></svg>Only high quality recordings of country music.</li>
    <li><svg width="20" height="20" viewBox="0 0 20 20"><circle cx="10" cy="10" r="10" fill="#2b55e0"/><path d="m5.5 10 3 3 6-6" stroke="#fff" stroke-width="2" fill="none"/></svg>Only unsigned artists.</li>
    <li><svg width="20" height="20" viewBox="0 0 20 20"><circle cx="10" cy="10" r="10" fill="#2b55e0"/><path d="m5.5 10 3 3 6-6" stroke="#fff" stroke-width="2" fill="none"/></svg>We strongly suggest the artist or band has a website or social media platforms.</li>
  </ul>
  <span class="btn">Launch Your Music</span>
  <svg class="abs q-arc" width="500" height="520" viewBox="0 0 500 520"><path d="M40 330a230 230 0 0 0 420 40" stroke="#2b55e0" stroke-width="36" fill="none"/></svg>
  <div class="abs q-photo" role="img" aria-label="Photo of a smiling guitarist in a hat giving a thumbs up"></div>
</section>

<section class="how">
  <h2 class="abs display"><b>How It</b> Works?</h2>

  <div class="abs step" style="top:200px">
    <div class="abs step-tab" style="left:0;border-top-right-radius:120px">
      <div class="abs lbl" style="left:30px;top:90px">Step<b>01</b></div>
      <div class="abs step-icon" style="left:170px;top:85px">
        <svg width="34" height="34" viewBox="0 0 24 24" fill="none" stroke="#2b55e0" stroke-width="1.8"><rect x="9" y="3" width="6" height="11" rx="3"/><path d="M5 11a7 7 0 0 0 14 0M12 18v3M8 21h8"/></svg>
      </div>
    </div>
    <p style="left:330px;top:40px">Submit 2 songs for review. If they are accepted, we want you to create an audio recording of your voice, giving our listeners a quick background on yourself, a little info about the songs and where people can find you and buy your music. (Don't worry, we will send you a form to read and record yourself where you'll just fill in the blanks about you and your songs). BTC takes care of the rest.</p>
  </div>

  <div class="abs step" style="top:520px">
    <div class="abs step-tab" style="right:0;border-top-left-radius:120px">
      <div class="abs step-icon" style="left:30px;top:85px">
        <svg width="34" height="34" viewBox="0 0 24 24" fill="none" stroke="#2b55e0" stroke-width="1.8"><path d="M4 14v-2a8 8 0 0 1 16 0v2"/><rect x="3" y="14" width="4" height="6" rx="1"/><rect x="17" y="14" width="4" height="6" rx="1"/></svg>
      </div>
      <div class="abs lbl" style="left:150px;top:90px">Step<b>02</b></div>
    </div>
    <p style="left:40px;top:60px">One of our international DJs will receive your two songs and audio file in your own voice. Our radio DJ will create a custom 10-minute feature, all about you, your songs and where listeners can find you and purchase your music.</p>
  </div>

  <div class="abs step" style="top:840px">
    <div class="abs step-tab" style="left:0;border-top-right-radius:120px">
      <div class="abs lbl" style="left:30px;top:90px">Step<b>03</b></div>
      <div class="abs step-icon" style="left:170px;top:85px">
        <svg width="34" height="34" viewBox="0 0 24 24" fill="none" stroke="#2b55e0" stroke-width="1.8"><circle cx="12" cy="12" r="9"/><path d="M8 16 16 8"/><circle cx="9" cy="9" r="1.3"/><circle cx="15" cy="15" r="1.3"/></svg>
      </div>
    </div>
    <p style="left:330px;top:50px">BTC does not receive any commission on your sales. Those are your sales. What if this exposure lands you a contract with a label or publisher? Great!! (We don't want a piece of that either.)<br><br>BTC is all about YOUR exposure. Worldwide exposure.</p>
  </div>
</section>

<section class="exposure">
  <div class="abs exp-mark">BTC</div>
  <div class="abs exp-frame"></div>
  <div class="abs exp-photo" role="img" aria-label="Photo of headphones resting on printed sheet music"></div>
  <h2 class="abs display">Get Over 4 1/2 Hours<br>Of Exposure Per Month</h2>
  <div class="abs sub">RIGHT NOW, FOR FREE</div>
  <ul class="abs ticks">
    <li><svg width="20" height="20" viewBox="0 0 20 20"><circle cx="10" cy="10" r="10" fill="#2b55e0"/><path d="m5.5 10 3 3 6-6" stroke="#fff" stroke-width="2" fill="none"/></svg>BTC provide you and your songs with international exposure.</li>
    <li><svg width="20" height="20" viewBox="0 0 20 20"><circle cx="10" cy="10" r="10" fill="#2b55e0"/><path d="m5.5 10 3 3 6-6" stroke="#fff" stroke-width="2" fill="none"/></svg>We are truly dedicated to getting your music out and your success.</li>
    <li><svg width="20" height="20" viewBox="0 0 20 20"><circle cx="10" cy="10" r="10" fill="#2b55e0"/><path d="m5.5 10 3 3 6-6" stroke="#fff" stroke-width="2" fill="none"/></svg>Artists receive 10 uninterrupted minutes of airtime EVERY DAY for 28 days. (This free offer to you may last longer)</li>
    <li><svg width="20" height="20" viewBox="0 0 20 20"><circle cx="10" cy="10" r="10" fill="#2b55e0"/><path d="m5.5 10 3 3 6-6" stroke="#fff" stroke-width="2" fill="none"/></svg>Artists will be given a schedule and link to your show to share on social media.</li>
    <li><svg width="20" height="20" viewBox="0 0 20 20"><circle cx="10" cy="10" r="10" fill="#2b55e0"/><path d="m5.5 10 3 3 6-6" stroke="#fff" stroke-width="2" fill="none"/></svg>Each day, your time slot will rotate forward by 3 hours, always be played in "prime-time" somewhere in the world.</li>
  </ul>
</section>

<section class="artists">
  <h2 class="abs display"><b>Artist</b> Profile</h2>
  <div class="abs artist" style="left:102px"><div class="frame"></div><div class="photo" role="img" aria-label="Photo of vocal artist Wade Carrow with a guitar" style="background:linear-gradient(160deg,#e9c07a,#8a5a34)"></div><h3>Wade Carrow</h3><span>Vocal Artist</span></div>
  <div class="abs artist" style="left:360px"><div class="frame"></div><div class="photo" role="img" aria-label="Photo of vocal artist Nell Brightly under stage lights" style="background:linear-gradient(160deg,#7a3fa8,#e04a7a)"></div><h3>Nell Brightly</h3><span>Vocal Artist</span></div>
  <div class="abs artist" style="left:618px"><div class="frame"></div><div class="photo" role="img" aria-label="Photo of vocal artist Teo Valdane in sunglasses" style="background:linear-gradient(160deg,#c9a27a,#4a3a30)"></div><h3>Teo Valdane</h3><span>Vocal Artist</span></div>
  <div class="abs artist" style="left:876px"><div class="frame"></div><div class="photo" role="img" aria-label="Photo of vocal artist Rina Osei in colourful outfit" style="background:linear-gradient(160deg,#3fb0c8,#d86a3a)"></div><h3>Rina Osei</h3><span>Vocal Artist</span></div>
  <span class="btn">View Our Artist</span>
</section>

<footer class="site-footer">
  <div class="abs brand">BTC</div>
  <div class="abs socials"><i></i><i></i><i></i></div>
  <div class="abs copyright">Copyright © 2022 BTC</div>
  <div class="abs f-divider" style="left:380px"></div>
  <div class="abs f-divider" style="left:760px"></div>
  <div class="abs links">
    <h4>Quick Links</h4>
    <ul><li>Home</li><li>Out Staff</li><li>Launch Your Music</li><li>FAQ</li><li>Artist Profiles</li></ul>
  </div>
  <div class="abs news">
    <h4>Newsletter</h4>
    <div class="field">Enter Email Address</div>
    <span class="btn">Subscribe Us!</span>
  </div>
</footer>

</body>
</html>
```